Seventy Crumbs needs a business card

Seventy Crumbs needs an attractive, playful, and exciting business card design to attract potential buyers. I have included our logo, label, and social media design files along with the fonts and colors for ideas. For the logo file, please only pay attention to the purple background with white text. I want a card with premium matte and metallic finish. I want my name included, e-mail, and phone number. The logo must be included, and then use the label design and social media design files to add creativity to the design. Only the fonts that are provided should be used as well.

Name: Gregory Talliston
Phone: 555-417-2086
E-mail: gtalliston@seventycrumbs.example

Contact Information for Business Card

I want a card with premium matte and metallic finish. I want my name included, e-mail, and phone number. The logo must be included, and then use the label design and social media design files to add creativity to the design. Only the fonts that are provided should be used as well.

Name: Gregory Talliston
Phone: 555-417-2086

Colors
6b449b

Requirements
Must have
• My logo, my fonts, my colors, my designs to some degree, and my character

```html
<!DOCTYPE html>
<html lang="en">
<head>
<meta charset="utf-8">
<title>Seventy Crumbs – Business Card</title>
<link href="https://fonts.googleapis.com/css2?family=Great+Vibes&family=Arimo:wght@400&display=swap" rel="stylesheet">
<style>
  :root {
    --page-bg: #e6e2dd;
    --frost-light: #f3f5f9;
    --frost-mid: #dfe4ec;
    --night-deep: #140d30;
    --night-mid: #261c52;
    --accent-blue: #2d62a3;
    --silver: #cfd3dc;
    --champagne: #dccbb7;
    --champagne-soft: #b9a892;
    --brand-purple: #2b2158;
  }
  * { margin: 0; padding: 0; box-sizing: border-box; }
  html, body {
    width: 1200px; height: 970px; overflow: hidden;
    background: var(--page-bg);
  }
  .card {
    position: absolute; left: 80px; top: 189px;
    width: 1040px; height: 592px;
    background: linear-gradient(160deg, var(--frost-light), var(--frost-mid));
    box-shadow: 0 14px 40px rgba(0,0,0,0.22);
    overflow: hidden;
  }
  .card-shapes { position: absolute; inset: 0; }
  .front-brand {
    position: absolute; left: 60px; top: 230px; width: 360px;
    display: flex; align-items: center; justify-content: center; gap: 14px;
  }
  .front-brand .dot {
    width: 26px; height: 26px; border-radius: 50%;
    background: var(--brand-purple);
  }
  .front-brand .name,
  .panel .brand {
    font-family: "Great Vibes", cursive;
    font-size: 64px; line-height: 1;
    color: var(--brand-purple);
  }
  .panel {
    position: absolute; left: 540px; top: 0; width: 430px; height: 100%;
    text-align: center; color: var(--champagne);
  }
  .panel .brand { position: absolute; left: 0; right: 0; top: 112px; font-size: 76px; color: var(--champagne); }
  .holder {
    position: absolute; left: 0; right: 0; top: 278px;
    font-family: "Great Vibes", cursive; font-size: 46px;
  }
  .label {
    position: absolute; left: 0; right: 0;
    font-family: "Great Vibes", cursive; font-size: 26px;
    color: var(--champagne-soft);
  }
  .value {
    position: absolute; left: 0; right: 0;
    font-family: "Arimo", sans-serif; font-size: 25px;
    color: var(--champagne-soft);
  }
  .label.phone { top: 370px; }
  .value.phone { top: 402px; }
  .divider {
    position: absolute; left: 20px; right: 14px; top: 441px;
    height: 1px; background: var(--champagne-soft);
  }
  .label.email { top: 458px; }
  .value.email { top: 499px; font-size: 24px; }
</style>
</head>
<body>
  <div class="card">
    <svg class="card-shapes" width="1040" height="592" viewBox="0 0 1040 592" aria-hidden="true">
      <defs>
        <linearGradient id="night" x1="0" y1="0" x2="1" y2="1">
          <stop offset="0" stop-color="#2c2160"/>
          <stop offset="0.5" stop-color="#1c1442"/>
          <stop offset="1" stop-color="#120b2b"/>
        </linearGradient>
      </defs>
      <path d="M440,0 C560,130 545,430 312,592 L1040,592 L1040,0 Z" fill="var(--accent-blue)"/>
      <path d="M452,0 C572,130 560,430 372,592 L1040,592 L1040,0 Z" fill="var(--silver)"/>
      <path d="M458,0 C578,130 566,430 382,592 L1040,592 L1040,0 Z" fill="url(#night)"/>
    </svg>

    <div class="front-brand">
      <span class="dot"></span>
      <span class="name">Seventy Crumbs</span>
    </div>

    <div class="panel">
      <div class="brand">Seventy Crumbs</div>
      <div class="holder">Gregory Talliston</div>
      <div class="label phone">Phone</div>
      <div class="value phone">555-417-2086</div>
      <div class="divider"></div>
      <div class="label email">Email</div>
      <div class="value email">gtalliston@seventycrumbs.example</div>
    </div>
  </div>
</body>
</html>
```